Landing Page Design für Ankauf-Shop von Metall (Schrott)
Zielgruppe
Ankauf Shop für Metall (Schrott) Versand mittels Paketversand.
Der Shop ist bereits vorhanden unter flinkmetall.de
Gesucht wird eine ansprechende Landing Page
Logo und Logofarbe sind bereits fest. ( siehe flinkmetall.de)
Footer muss nicht dabei sein, ein Textfeld mit dem Begriff „wie gehts“ muss vorhanden sein, damit der Kundschaft erklärt werden kann, wie der Ablauf ist.
Das Design wird benötig für Desktop, Tablet und Smartphone.
Aufgabenstellung
Klarheit, Übersichtlichkeit, ansprechendes Design,

```html
<!DOCTYPE html>
<html lang="de">
<head>
<meta charset="utf-8">
<title>flinkmetall.de – Online Schrott verkaufen</title>
<link href="https://fonts.googleapis.com/css2?family=Barlow+Semi+Condensed:wght@400;500;600;700&display=swap" rel="stylesheet">
<style>
  :root {
    --green: #6fb12a;
    --green-dark: #5c9a1f;
    --green-light: #7dbd34;
    --ink: #222222;
    --title-bg: #262626;
    --bar-bg: #eef4fb;
    --page-bg: #dde9f4;
    --card: #ffffff;
    --steel: #5f5f5f;
    --steel-light: #cfcfcf;
    --muted: #5a5a5a;
  }
  * { box-sizing: border-box; margin: 0; padding: 0; }
  html, body { width: 1200px; height: 744px; overflow: hidden; }
  body { font-family: "Barlow Semi Condensed", sans-serif; color: var(--ink); background: var(--page-bg); position: relative; }

  .site-header { position: absolute; left: 0; top: 0; width: 1200px; height: 80px; background: linear-gradient(180deg, var(--green-light), var(--green)); }
  .nav-primary { position: absolute; left: 132px; top: 26px; display: flex; align-items: center; gap: 16px; }
  .nav-primary .btn-sell { background: #fff; color: var(--ink); font-size: 15px; font-weight: 500; padding: 4px 8px; height: 28px; line-height: 20px; border-radius: 2px; }
  .nav-primary .link-how { color: #fff; font-size: 15px; font-weight: 500; }
  .brand { position: absolute; left: 505px; top: 22px; display: flex; align-items: center; gap: 8px; color: #fff; font-size: 20px; font-weight: 700; }
  .brand-dot { width: 34px; height: 34px; border-radius: 50%; background: #fff; }
  .header-icons { position: absolute; left: 944px; top: 28px; display: flex; gap: 12px; }
  .header-icons svg { width: 22px; height: 22px; stroke: #fff; fill: none; stroke-width: 1.6; }
  .tooltip { position: absolute; left: 994px; top: 57px; background: var(--title-bg); color: #fff; font-size: 11px; padding: 2px 6px; border-radius: 2px; }

  .usp-bar { position: absolute; left: 0; top: 80px; width: 1200px; height: 48px; background: var(--bar-bg); }
  .usp { position: absolute; top: 16px; display: flex; align-items: center; gap: 6px; font-size: 12px; font-weight: 500; }
  .usp svg { width: 16px; height: 16px; stroke: var(--ink); fill: none; stroke-width: 1.6; }

  .process-card { position: absolute; left: 120px; top: 176px; width: 960px; height: 400px; background: var(--card); border-radius: 3px; box-shadow: 0 8px 14px rgba(60,90,120,.15); }
  .process-banner { position: absolute; left: 4px; top: 4px; width: 952px; height: 140px; background: linear-gradient(135deg, #d8d8d8, #f2f2f2 40%, #c9c9c9 70%, #e8e8e8); border-bottom: 5px solid var(--green); }
  .process-title { position: absolute; left: 238px; top: 41px; width: 501px; height: 61px; background: var(--title-bg); color: #fff; font-size: 38px; font-weight: 500; text-align: center; line-height: 61px; }
  .process-title em { font-style: normal; font-weight: 700; color: var(--green); }
  .how-label { position: absolute; left: 422px; top: 122px; width: 144px; height: 42px; background: var(--green); color: #fff; font-size: 18px; font-weight: 500; text-align: center; line-height: 42px; box-shadow: 0 1px 2px rgba(0,0,0,.2); }

  .steps-line { position: absolute; left: 120px; top: 256px; width: 720px; height: 2px; background: var(--green); }
  .step-check { position: absolute; top: 245px; width: 24px; height: 24px; border-radius: 50%; background: var(--green); }
  .step-check svg { width: 24px; height: 24px; stroke: #fff; fill: none; stroke-width: 2.5; }
  .step { position: absolute; top: 195px; width: 220px; text-align: center; }
  .step-visual { width: 116px; height: 116px; margin: 0 auto; border-radius: 50%; border: 4px solid var(--green); background: radial-gradient(circle, #8a8a8a, var(--steel)); }
  .step-text { margin-top: 10px; font-size: 15px; line-height: 16px; font-weight: 500; }

  .cta-section { position: absolute; left: 0; top: 624px; width: 1200px; height: 120px; background: #fff; }
  .cta-slant { position: absolute; left: 0; top: 0; }
  .cta-button { position: absolute; left: 212px; top: 33px; width: 308px; height: 56px; background: var(--green); border: 1px solid var(--green-dark); border-radius: 2px; color: #fff; font-size: 22px; font-weight: 500; display: flex; }
  .cta-button span { flex: 1; line-height: 54px; padding-left: 18px; }
  .cta-button .cta-arrow { width: 66px; border-left: 1px solid var(--green-dark); display: flex; align-items: center; justify-content: center; }
  .cta-arrow svg { width: 34px; height: 28px; stroke: #fff; fill: none; stroke-width: 3; }
  .hotline { position: absolute; left: 715px; top: 37px; color: var(--muted); }
  .hotline-label { font-size: 12px; font-weight: 500; }
  .hotline-number { font-size: 38px; font-weight: 500; line-height: 36px; }
</style>
</head>
<body>
  <header class="site-header">
    <nav class="nav-primary">
      <span class="btn-sell">Metalle verkaufen</span>
      <span class="link-how">Wie?</span>
    </nav>
    <div class="brand"><span class="brand-dot"></span>flinkmetall.de</div>
    <div class="header-icons">
      <svg viewBox="0 0 24 24"><circle cx="10" cy="10" r="7"/><path d="M15 15l6 6"/></svg>
      <svg viewBox="0 0 24 24"><path d="M4 14v-3a8 8 0 0 1 16 0v3"/><rect x="3" y="13" width="4" height="6" rx="1"/><rect x="17" y="13" width="4" height="6" rx="1"/></svg>
      <svg viewBox="0 0 24 24"><circle cx="12" cy="12" r="10"/><circle cx="12" cy="10" r="3.5"/><path d="M5.5 19a7.5 6 0 0 1 13 0"/></svg>
      <svg viewBox="0 0 24 24"><path d="M2 4h3l3 11h11l2-8H6"/><circle cx="9" cy="20" r="1.3"/><circle cx="18" cy="20" r="1.3"/></svg>
    </div>
    <div class="tooltip">Mein Konto</div>
  </header>

  <section class="usp-bar">
    <div class="usp" style="left:132px"><svg viewBox="0 0 24 24"><path d="M1 6h13v10H1zM14 10h5l3 3v3h-8"/><circle cx="5" cy="18" r="2"/><circle cx="18" cy="18" r="2"/></svg>Einfacher Versand</div>
    <div class="usp" style="left:342px"><svg viewBox="0 0 24 24"><circle cx="12" cy="12" r="10"/><path d="M12 6v6h5"/></svg>Schnelle Auszahlung</div>
    <div class="usp" style="left:561px"><svg viewBox="0 0 24 24"><path d="M2 10h4v11H2zM6 10l5-8c2 0 3 1 2.5 3L13 9h7c1 0 2 1 1.7 2.2l-2 8c-.3 1-1 1.8-2 1.8H6"/></svg>Aktuelle Preise</div>
    <div class="usp" style="left:755px"><svg viewBox="0 0 24 24"><rect x="2" y="3" width="5" height="18"/><rect x="7" y="3" width="15" height="18"/><path d="M10 7h9M10 11h3M15 11h4M10 15h3M15 15h4"/></svg>Konstenlose Hotline</div>
    <div class="usp" style="left:969px"><svg viewBox="0 0 24 24" style="fill:var(--ink);stroke:none"><path d="M20 16l-4-2-2 2c-3-1.5-5.5-4-7-7l2-2-2-4H3c0 10 8 18 18 18v-4z"/></svg>0800 - 765 432 100</div>
  </section>

  <main class="process-card">
    <div class="process-banner" role="img" aria-label="Gebürstete Metalloberfläche als Hintergrund">
      <h1 class="process-title">Online <em>flink</em> Schrott verkaufen</h1>
    </div>
    <div class="how-label">So einfach geht’s</div>

    <div class="steps-line"></div>
    <div class="step-check" style="left:233px"><svg viewBox="0 0 24 24"><path d="M7 12l3.5 3.5L17 9"/></svg></div>
    <div class="step-check" style="left:478px"><svg viewBox="0 0 24 24"><path d="M7 12l3.5 3.5L17 9"/></svg></div>
    <div class="step-check" style="left:714px"><svg viewBox="0 0 24 24"><path d="M7 12l3.5 3.5L17 9"/></svg></div>

    <div class="step" style="left:10px">
      <div class="step-visual" role="img" aria-label="Symbol Benutzerprofil"></div>
      <p class="step-text">Kostenlos auf <b>flink</b>metall<br>registrieren</p>
    </div>
    <div class="step" style="left:260px">
      <div class="step-visual" role="img" aria-label="Symbol Formular mit Stift"></div>
      <p class="step-text">Anmelden und Formular<br>ausfüllen</p>
    </div>
    <div class="step" style="left:501px">
      <div class="step-visual" role="img" aria-label="Symbol Sackkarre mit Paketen"></div>
      <p class="step-text">Gewünschte Versandart<br>auswählen</p>
    </div>
    <div class="step" style="left:730px">
      <div class="step-visual" role="img" aria-label="Symbol Bankkarte"></div>
      <p class="step-text">Auszahlung auf Ihr<br>Bankkonto</p>
    </div>
  </main>

  <section class="cta-section">
    <svg class="cta-slant" width="1200" height="120" viewBox="0 0 1200 120"><polygon points="632,0 1200,0 1200,120 585,120" fill="var(--bar-bg)"/></svg>
    <div class="cta-button">
      <span>Jetzt Metalle verkaufen</span>
      <div class="cta-arrow"><svg viewBox="0 0 34 28"><path d="M2 14h29M19 3l12 11-12 11"/></svg></div>
    </div>
    <div class="hotline">
      <p class="hotline-label">Kostenlose Hotline:</p>
      <p class="hotline-number">0800 - 765 432 100</p>
    </div>
  </section>
</body>
</html>
```